Maplerise Trading Inc. needs an innovative idea for letterhead and visiting cards.

Maplerise Trading Inc. is a Canadian brand since 2007. It is a renown dealer of kids and office furniture locally. Moreover, exporting electric fixtures e.g. switches, LED's, down-lights etc. to Middle East and Africa. We have initiated a number of steps including re-branding, to boost our export in 2020. We have successfully designed our new logo a few months ago through 'Artfolio' and now we are looking for an innovative idea for a letterhead.
Some key points:
• Red, black and white are the three colors used in all our packaging and furniture. (grey is optional)
• Shouldn’t be too wide.
• Use of watermark is preferable.
• You can visit our North American site at www.mapleriseinc.com. Export website of the company will be launched soon. www.mapleriseinc.ca
• Same letterhead will be used locally and internationally.
• Our new logo and sample packaging is attached.

```html
<!DOCTYPE html>
<html lang="en">
<head>
<meta charset="utf-8">
<title>Maplerise Trading – Letterhead &amp; Envelope</title>
<link href="https://fonts.googleapis.com/css2?family=Open+Sans:wght@400&family=Lato:wght@400;700&family=Montserrat:wght@300&display=swap" rel="stylesheet">
<style>
  :root {
    --red: #a30d14;
    --charcoal: #444446;
    --ink: #4a4a4a;
    --text: #5a5a5a;
    --paper: #ffffff;
    --stage: #e6e6e8;
    --rule: #d9d9d9;
  }
  * { margin: 0; padding: 0; box-sizing: border-box; }
  html, body { width: 1200px; height: 1200px; overflow: hidden; }
  body { background: var(--stage); position: relative; font-family: "Open Sans", sans-serif; }

  .sheet { position: absolute; background: var(--paper); box-shadow: 0 4px 18px rgba(0,0,0,.18); }

  /* Letterhead */
  .letterhead { left: 40px; top: 190px; width: 640px; height: 822px; }
  .letterhead .top-bar { position: absolute; left: 0; top: 0; width: 100%; height: 12px; background: var(--charcoal); }
  .letterhead .bottom-bar { position: absolute; left: 0; bottom: 0; width: 100%; height: 14px; background: var(--red); }

  .brand { position: absolute; display: flex; align-items: center; gap: 8px; }
  .brand .mark { width: 46px; height: 46px; border: 2px solid var(--red); border-radius: 4px; }
  .brand .name { font-family: "Montserrat", sans-serif; font-weight: 300; color: var(--charcoal); line-height: 1.05; letter-spacing: .5px; }
  .letterhead .brand { left: 226px; top: 22px; }
  .letterhead .brand .name { font-size: 24px; }

  .letter { position: absolute; left: 60px; top: 150px; width: 518px; font-size: 10.4px; color: var(--text); }
  .letter p { line-height: 18.4px; }
  .letter .date { margin-bottom: 10px; }
  .letter .recipient { line-height: 12.5px; margin-bottom: 36px; }
  .letter .salutation { margin-bottom: 18px; }
  .letter .body-copy { text-align: justify; margin-bottom: 18px; }
  .letter .closing { margin-top: 28px; }
  .signature { width: 148px; height: 20px; margin: 8px 0 6px; background: linear-gradient(90deg, #cfcfd2, #e4e4e6); border-radius: 3px; }
  .signer { font-size: 12.4px; color: var(--ink); line-height: 18px; }
  .title { font-size: 10.4px; color: var(--text); line-height: 18px; }

  .footer { position: absolute; left: 0; width: 100%; top: 766px; text-align: center; font-family: "Lato", sans-serif; font-size: 12px; color: #333; }
  .footer .address { padding-bottom: 2px; }
  .footer .rule { width: 376px; height: 1px; background: var(--rule); margin: 0 auto 3px; }
  .footer .label { color: var(--red); }
  .footer .web { color: var(--red); }

  /* Envelope front */
  .envelope-front { left: 720px; top: 380px; width: 440px; height: 220px; }
  .envelope-front .top-bar { position: absolute; left: 0; top: 0; width: 100%; height: 6px; background: var(--charcoal); }
  .envelope-front .bottom-bar { position: absolute; left: 0; bottom: 0; width: 100%; height: 7px; background: var(--red); }
  .envelope-front .brand { left: 26px; top: 14px; gap: 6px; }
  .envelope-front .brand .mark { width: 34px; height: 34px; }
  .envelope-front .brand .name { font-size: 17px; }
  .envelope-front .return-address { position: absolute; left: 26px; top: 195px; font-family: "Lato", sans-serif; font-size: 8.6px; color: #333; }

  /* Envelope back */
  .envelope-back { left: 722px; top: 640px; width: 436px; height: 217px; }
  .envelope-back .flap-band { position: absolute; left: 0; top: 0; width: 100%; height: 51px; background: var(--red); clip-path: polygon(0 0, 100% 0, 96% 100%, 4% 100%); }
</style>
</head>
<body>

  <section class="sheet letterhead">
    <div class="top-bar"></div>
    <div class="brand">
      <div class="mark"></div>
      <div class="name">Maplerise<br>Trading</div>
    </div>

    <div class="letter">
      <p class="date">Issuing Date: May 5, 2018</p>
      <div class="recipient">
        <p>Name Of Employee Mr. XYZABC</p>
        <p>Address of Employee</p>
        <p>Address Line 2 etc..</p>
      </div>
      <p class="salutation">Dear Mr.XYZABC</p>
      <p class="body-copy">Lorem Ipsum has been the industry's standard dummy text ever since the 1500s, when an unknown printer took a galley of type and scrambled it to make a type specimen book. It has survived not only five centuries, but also the leap into electronic typesetting, remaining essentially unchanged. It was popularised in the 1960s with the release of Letraset sheets containing Lorem Ipsum passages, and more recently with desktop publishing software like Aldus PageMaker including versions of Lorem Ipsum.</p>
      <p class="body-copy">Lorem Ipsum is simply dummy text of the printing and typesetting industry. Lorem Ipsum has been the industry's standard dummy text ever since the 1500s, when an unknown printer took a galley of type and scrambled it to make a type specimen book.</p>
      <p class="body-copy">It has survived not only five centuries, but also the leap into electronic typesetting, remaining essentially unchanged. It was popularised in the 1960s with the release of Letraset sheets containing Lorem Ipsum passages.</p>
      <p class="closing">Yours Sincerely</p>
      <div class="signature" role="img" aria-label="Handwritten signature of Daniel Whitmore"></div>
      <p class="signer">Daniel Whitmore</p>
      <p class="title">Managing Director</p>
    </div>

    <div class="footer">
      <p class="address">421, Address line goes here Country Name, 45452</p>
      <div class="rule"></div>
      <p><span class="label">P:</span> 041-552 318 907 | <span class="label">E:</span> hello@mapleriseinc.com | <span class="web">www.mapleriseinc.com</span></p>
    </div>
    <div class="bottom-bar"></div>
  </section>

  <section class="sheet envelope-front">
    <div class="top-bar"></div>
    <div class="brand">
      <div class="mark"></div>
      <div class="name">Maplerise<br>Trading</div>
    </div>
    <p class="return-address">421, Address line goes here Country Name, 45452</p>
    <div class="bottom-bar"></div>
  </section>

  <section class="sheet envelope-back">
    <div class="flap-band"></div>
  </section>

</body>
</html>
```